Land Buying Company Needs Letterhead for Direct Mail Marketing to Land Owners

We are looking for a professional letterhead that we will be including in our direct mail marketing. We will be sending this to land owners who may be interested in selling or purchasing land.

The letterhead needs to be editable. Headers and footers would look nice, but we are open. We would want it to include our address, website, phone, and email info. For right now the address to use for design purposes would the following:

Address: 415 Bramwell Avenue #600
Dallas, TX 75219
Website - www.quillridgeacres.example
Email - info@quillridgeacres.example
Phone - 866-402-ACRE

I have attached our logo zip file that we just had done on Pixel Guild. Let me know what questions you have, and thank you.

```html
<!DOCTYPE html>
<html lang="en">
<head>
<meta charset="utf-8">
<title>Quillridge Acres Letterhead</title>
<link href="https://fonts.googleapis.com/css2?family=Montserrat:wght@400;700&family=Lato:wght@300;400;700&family=Great+Vibes&display=swap" rel="stylesheet">
<style>
  :root {
    --backdrop: #e4e6e8;
    --paper: #f2f2f2;
    --brand-green: #8cc63f;
    --brand-dark: #3f5a2a;
    --ink: #1c1c1c;
    --muted: #8a8a8a;
    --contact: #5a5a5a;
    --forest: #3b4f5c;
    --forest-light: #45606e;
    --watermark: #e8e8e8;
  }
  * { box-sizing: border-box; margin: 0; padding: 0; }
  html, body { width: 1200px; height: 1200px; overflow: hidden; background: var(--backdrop); }
  .letterhead {
    position: absolute; left: 205px; top: 41px;
    width: 790px; height: 1118px;
    background: var(--paper);
    overflow: hidden;
    font-family: "Lato", sans-serif;
  }
  .brand {
    position: absolute; left: 50px; top: 63px;
    display: flex; align-items: center; gap: 12px;
  }
  .brand-dot { width: 52px; height: 52px; border-radius: 50%; background: var(--brand-dark); }
  .brand-name {
    font-family: "Montserrat", sans-serif; font-weight: 700;
    font-size: 26px; color: var(--brand-green); letter-spacing: 0.5px;
  }
  .contact {
    position: absolute; left: 526px; top: 44px;
    border-left: 1.5px solid var(--brand-green);
    padding-left: 16px;
    font-family: "Montserrat", sans-serif; font-size: 12px;
    color: var(--contact); line-height: 16px;
  }
  .contact .address { margin-bottom: 7px; padding-top: 1px; }
  .contact li { list-style: none; display: flex; align-items: center; gap: 7px; }
  .contact svg { width: 10px; height: 10px; fill: var(--brand-green); flex: none; }
  .watermark {
    position: absolute; left: 213px; top: 360px;
    width: 382px; height: 382px; border-radius: 50%;
    background: var(--watermark);
  }
  .letter {
    position: absolute; left: 84px; right: 85px; top: 243px;
    font-size: 12.5px; line-height: 18.6px; color: var(--muted); font-weight: 300;
  }
  .letter .date { margin-bottom: 19px; }
  .recipient { margin-bottom: 37px; }
  .recipient strong { color: var(--ink); font-weight: 700; display: block; }
  .salutation { margin-bottom: 18px; }
  .letter p.body { text-align: justify; margin-bottom: 18.6px; font-weight: 400; color: #9a9a9a; }
  .closing { margin-top: 48px; }
  .signature {
    font-family: "Great Vibes", cursive; font-size: 27px;
    color: var(--ink); margin-top: 4px; padding-left: 6px; font-weight: 400;
  }
  .forest-band {
    position: absolute; left: 0; right: 0; bottom: 0; height: 104px;
    background: linear-gradient(to bottom, var(--forest), var(--forest-light));
  }
</style>
</head>
<body>
  <main class="letterhead">
    <div class="brand">
      <span class="brand-dot"></span>
      <span class="brand-name">Quillridge Acres</span>
    </div>

    <address class="contact" style="font-style:normal">
      <div class="address">415 Bramwell Avenue #600<br>Dallas, TX 75219</div>
      <ul>
        <li><svg viewBox="0 0 10 10"><path d="M2 0.5 L3.6 2.6 L2.8 3.6 Q4 5.9 6.3 7.1 L7.3 6.3 L9.5 7.9 L8.4 9.5 Q3.5 9 0.5 1.6 Z"/></svg>866-402-ACRE</li>
        <li><svg viewBox="0 0 10 10"><path d="M0 2 H10 V8 H0 Z M0.6 2.4 L5 5.6 L9.4 2.4" stroke="#f2f2f2" stroke-width="0.8"/></svg>info@quillridgeacres.example</li>
        <li><svg viewBox="0 0 10 10"><circle cx="5" cy="5" r="4.6"/><path d="M0.6 5 H9.4 M5 0.5 V9.5 M5 0.5 Q2 5 5 9.5 M5 0.5 Q8 5 5 9.5" stroke="#f2f2f2" stroke-width="0.6" fill="none"/></svg>www.quillridgeacres.example</li>
      </ul>
    </address>

    <div class="watermark" aria-hidden="true"></div>

    <section class="letter">
      <div class="date">01 January 2050</div>
      <div class="recipient">
        <strong>Company (Pvt) Ltd.</strong>
        PO Box 3355 Mainville St<br>
        Sample City Country 3355
      </div>
      <div class="salutation">Dear Dana Whitfield,</div>
      <p class="body">Lorem ipsum dolor sit amet, consectetuer adipiscing elit, sed diam nonummy nibh euismod tincidunt ut laoreet dolore magna aliquam erat volutpat. Ut wisi enim ad minim veniam, quis nostrud exerci tation ullamcorper suscipit lobortis nisl ut aliquip ex ea commodo consequat. Duis dolore te feugait nulla facilisi. Nam liber tempor cum soluta nobis eleifend option congue nihil imperdiet doming id quod mazim placerat facer possim assum. Lorem ipsum dolor sit amet, consectetuer adipiscing elit, sed diam nonummy nibh euismod tincidunt ut laoreet dolore magna aliquam erat volutpat. Ut wisi enim ad minim veniam, quis nostrud exerci tation ullamcorper suscipit lobortis nisl ut aliquip ex ea commodo consequat.</p>
      <p class="body">Consectetuer adipiscing elit, sed diam nonummy nibh euismod tincidunt ut laoreet dolore magna aliquam erat volutpat. Ut wisi enim ad minim veniam, quis nostrud exerci tation ullamcorper suscipit lobortis nisl ut aliquip ex ea commodo consequat. Consectetuer adipiscing elit, sed diam nonummy nibh euismod tincidunt ut laoreet dolore magna aliquam erat volutpat. Ut wisi enim ad minim veniam, quis nostrud exerci tation ullamcorper suscipit lobortis nisl ut aliquip ex ea commodo consequat.</p>
      <p class="body">Consectetuer adipiscing elit, sed diam nonummy nibh euismod tincidunt ut laoreet dolore magna aliquam erat volutpat. Ut wisi enim ad minim veniam, quis nostrud exerci tation ullamcorper suscipit lobortis nisl ut aliquip ex ea commodo consequat. Consectetuer adipiscing elit, sed diam nonummy nibh euismod tincidunt ut laoreet dolore magna aliquam erat volutpat. Ut wisi enim ad minim veniam, quis nostrud exerci tation ullamcorper suscipit lobortis nisl ut aliquip ex ea commodo consequat.</p>
      <div class="closing">Sincerely Yours</div>
      <div class="signature">Marcus Ellery Brandt</div>
    </section>

    <div class="forest-band" role="img" aria-label="Footer illustration of a row of pine tree silhouettes in slate blue"></div>
  </main>
</body>
</html>
```